Website Design Project For New Online Service
World Wide Online Obituary Notification Service Needing Professional Design
Website Design Project For New Online Service  - Internet Services
Creative Brief
Internet Services
http://www.MournBeacon.net
MournBeacon.net is an online obituary notification service.
Mournbeacon.net was created because there are far too many situations where someone says something like "why isn't your husband golfing with us today?" which is responded to by "he passed away 2 years ago."
This is awkward and hurtful for everyone involved. But it isn't the individuals fault! Society depends on newspapers for this information and nowadays it seems like another newspapers is declaring bankruptcy every month. They just don't work with todays fast paced lifestyle! So what does work with todays lifestyle? email, texting, tweeting and other electronic communication that delivers the information you want, when you want it!
MournBeacon allows individuals to sign up for an account and upload their email contact list from any major provider and receive a notification directly to their email if someone from this list passes away. Saving you the time of checking obituaries and keeping you informed!
MournBeacon.net "Stay close to those you love"
Modern
Blue (as seen in our symbol)
Grey (as seen in out symbol)
Looking forward to seeing the entries. Thanks to everyone who submits something!

```html
<!DOCTYPE html>
<html lang="en">
<head>
<meta charset="utf-8">
<title>MournBeacon.net – Obituary Notification Service</title>
<link rel="stylesheet" href="https://fonts.googleapis.com/css2?family=Cinzel:wght@400;600&family=Noto+Serif:wght@400;700&family=Open+Sans:wght@300;400;600;700&display=swap">
<style>
  :root{
    --navy:#1c3961;
    --navy-mid:#2b4d7a;
    --nav-blue:#35598a;
    --brand-blue:#2c69a8;
    --text-blue:#2f5d8e;
    --accent-pink:#d8334f;
    --signin-red:#c6242c;
    --page-grey:#e8ecef;
    --panel-grey:#f1f2f3;
    --line-grey:#c9ced3;
    --body-text:#565b60;
    --footer-text:#3d4a58;
    --white:#ffffff;
  }
  *{margin:0;padding:0;box-sizing:border-box;}
  html,body{width:1200px;height:923px;overflow:hidden;}
  body{position:relative;background:var(--white);font-family:"Open Sans",Arial,sans-serif;}

  .hero-band{position:absolute;left:0;top:0;width:1200px;height:380px;overflow:hidden;
    background:linear-gradient(180deg,#f4f6f8 0%,#e3e9ee 60%,#d9e0e6 100%);}
  .hero-art{position:absolute;left:740px;top:100px;width:280px;height:280px;
    background:radial-gradient(ellipse at 50% 40%,#efe4d6 0%,#c9dab4 35%,rgba(217,224,230,0) 68%);}

  .site-header{position:absolute;left:170px;top:0;width:880px;height:100px;z-index:2;}
  .header-top{height:70px;background:linear-gradient(180deg,#3a5f8f 0%,var(--navy) 100%);position:relative;}
  .brand{position:absolute;left:14px;top:10px;display:flex;align-items:center;gap:8px;}
  .brand-mark{width:30px;height:30px;border-radius:50%;background:#a9b6c4;}
  .brand-name{font-weight:600;font-size:24px;color:var(--white);line-height:1;}
  .brand-tag{position:absolute;left:52px;top:44px;font-size:10px;color:#c6d2df;}
  .contact{position:absolute;right:18px;top:10px;color:var(--white);}
  .contact .label{font-size:10px;color:#c6d2df;}
  .contact .phone{font-size:20px;font-weight:700;line-height:1.05;}
  .contact .email{font-size:10px;color:#c6d2df;}
  .main-nav{height:30px;background:linear-gradient(180deg,var(--nav-blue),#294a76);display:flex;justify-content:center;}
  .main-nav a{color:var(--white);text-decoration:none;font-size:12px;line-height:30px;padding:0 30px;}

  .hero-copy{position:absolute;left:256px;top:140px;width:470px;z-index:1;}
  .hero-title{font-weight:300;font-size:76px;color:var(--accent-pink);line-height:1;letter-spacing:-1px;}
  .hero-sub{font-weight:300;font-size:34px;color:var(--text-blue);margin-left:112px;line-height:1.1;}
  .hero-text{margin-top:22px;font-size:13px;font-weight:600;color:var(--text-blue);line-height:18px;width:310px;}

  .welcome{position:absolute;left:0;top:405px;width:1200px;text-align:center;}
  .welcome h1{font-family:"Cinzel",serif;font-weight:400;font-size:36px;color:var(--brand-blue);letter-spacing:1px;line-height:44px;}
  .welcome p{width:650px;margin:22px auto 0;font-family:"Noto Serif",Georgia,serif;font-size:12.5px;line-height:19px;color:var(--body-text);}

  .accounts-row{position:absolute;left:0;top:603px;width:1200px;height:202px;background:var(--page-grey);}
  .account-box{position:absolute;top:9px;height:184px;background:var(--panel-grey);border:1px solid var(--line-grey);overflow:hidden;}
  .account-box h2{font-family:"Noto Serif",Georgia,serif;font-weight:400;font-size:16px;color:#3c3f42;text-align:center;
    background:var(--white);height:32px;line-height:31px;border-bottom:1px solid var(--line-grey);}
  .account-box p{font-family:"Noto Serif",Georgia,serif;font-size:10px;line-height:13px;color:var(--body-text);padding:8px 12px 0;}
  .box-button{display:block;margin:8px auto 0;background:linear-gradient(180deg,#4a7bb6,#2e5c96);color:var(--white);
    font-size:9.5px;font-weight:600;text-align:center;padding:4px 10px;border-radius:2px;width:fit-content;border:1px solid #24497a;}
  .funeral{left:250px;width:272px;}
  .users{left:530px;width:244px;}
  .users p{padding:8px 10px 0;}

  .login-box{position:absolute;left:782px;top:9px;width:232px;height:184px;background:var(--navy-mid);border:1px solid #1a3357;}
  .login-box h2{font-family:"Noto Serif",Georgia,serif;font-weight:400;font-size:18px;color:var(--white);text-align:center;
    background:var(--navy);height:34px;line-height:34px;}
  .field{display:flex;align-items:center;justify-content:flex-end;padding:7px 20px 0 0;gap:6px;}
  .field label{font-size:11px;color:var(--white);}
  .field span{display:block;width:118px;height:16px;background:var(--white);border:1px solid #9fb0c4;}
  .signin{margin:9px 0 0 96px;background:var(--signin-red);color:var(--white);font-size:10px;font-weight:600;padding:3px 10px;border-radius:2px;display:inline-block;}
  .login-links{list-style:none;margin:10px 0 0 18px;}
  .login-links li{font-size:10px;color:var(--white);line-height:14px;}
  .login-links li::before{content:"» ";}

  .site-footer{position:absolute;left:0;top:805px;width:1200px;height:118px;background:#dde2e6;border-top:1px solid #c4cad0;}
  .footer-links{position:absolute;left:170px;top:30px;display:flex;gap:6px;font-size:11.5px;color:var(--footer-text);}
  .footer-links .sep{color:#8b96a2;}
  .legal{position:absolute;left:170px;top:54px;font-size:8px;line-height:12px;color:#6b7580;}
  .badges{position:absolute;left:782px;top:10px;width:232px;height:98px;background:var(--white);border:1px solid #c4cad0;
    display:flex;align-items:center;justify-content:space-around;}
  .badge-plain{background:#cfd6dd;}
  .badge-square{width:56px;height:40px;border-radius:3px;}
  .badge-tall{width:36px;height:56px;border-radius:3px;}
  .badge-round{width:60px;height:60px;border-radius:50%;}
</style>
</head>
<body>
  <div class="hero-band">
    <div class="hero-art" role="img" aria-label="Photo of a hand holding a small bouquet of wildflowers"></div>
  </div>

  <header class="site-header">
    <div class="header-top">
      <div class="brand">
        <span class="brand-mark"></span>
        <span class="brand-name">MournBeacon.net</span>
      </div>
      <span class="brand-tag">stay close to those you love</span>
      <div class="contact">
        <div class="label">Toll Free:</div>
        <div class="phone">1 800 555 0142</div>
        <div class="email">email: info@mournbeacon.net</div>
      </div>
    </div>
    <nav class="main-nav">
      <a href="#">Home</a><a href="#">How it Works</a><a href="#">FAQ</a><a href="#">Help</a><a href="#">Contact Us</a>
    </nav>
  </header>

  <section class="hero-copy">
    <div class="hero-title">Everyone</div>
    <div class="hero-sub">has had a time when...</div>
    <p class="hero-text">you are sending out christmas cards and you are not sure of the health of someone you are sending it to or their immediate family.</p>
  </section>

  <section class="welcome">
    <h1>Welcome to MournBeacon</h1>
    <p>It's simple! Sign up for a free account and upload your contacts. You can upload your contacts manually, or import them from postloft, quillmail, yondermail, ZMX, or even deskpost! Once you have uploaded your contacts, your account is complete. Remember, you can update your contact list and add additional contacts at anytime.</p>
  </section>

  <section class="accounts-row">
    <div class="account-box funeral">
      <h2>Funeral Home Accounts</h2>
      <p>Traditional methods of obituaries are no longer keeping up with our society. We don't have time to be checking all the newspapers of where our friends, family or even clients are located. But we still need to be informed when someone passes away.</p>
      <p>Join the Next Generation Obituary Notification Service.</p>
      <span class="box-button">Register a Funeral Home Account</span>
    </div>
    <div class="account-box users">
      <h2>User Accounts</h2>
      <p>Checking the obituaries too often? Worrying that you'll miss an obituary? Here is your peace of mind! Mournbeacon.net eliminates those concerns by notifying you in the unfortunate event that a friend, colleague or loved one passes away.</p>
      <span class="box-button">Sign up for an MournBeacon.net account</span>
    </div>
    <div class="login-box">
      <h2>Login</h2>
      <div class="field"><label>Email:</label><span></span></div>
      <div class="field"><label>Password:</label><span></span></div>
      <span class="signin">Sign in</span>
      <ul class="login-links">
        <li>Create Basic Account</li>
        <li>Forgot Password</li>
        <li>Funeral Home Registration</li>
      </ul>
    </div>
  </section>

  <footer class="site-footer">
    <div class="footer-links">
      <span>Our Services</span><span class="sep">|</span><span>Return Policy</span><span class="sep">|</span><span>Delivery Policy</span><span class="sep">|</span><span>Privacy Policy</span><span class="sep">|</span><span>Contact Us</span>
    </div>
    <div class="legal">
      Copyright © 2012 MournBeacon.net All rights reserved.<br>
      Trademarks of MournBeacon Holdings. Used under license by Harbor Lane Media, Inc. and MournBeacon.net
    </div>
    <div class="badges">
      <span class="badge-plain badge-square"></span>
      <span class="badge-plain badge-tall"></span>
      <span class="badge-plain badge-round"></span>
    </div>
  </footer>
</body>
</html>
```